Real Estate Oversized Postcard

We are a new Real estate development firm looking to put together a postcard for mailings. The front of the card will look very similar to the front page on our website at www.torvelgroup.com. Use that main photo and "Flexible and Focused' as well as our logo somewhere. The back of the card should look like the DWP Urgent Care postcard attachment. Put our logo on the top. Then "With years of experience developing healthcare projects across America, we are ready to tackle any challenge our clients may present." Add our contact information to the bottom as well: Torvel Group, LLC, 3817 Marlow Avenue, Suite 240, Palm Beach Gardens, FL 33962 561-384-2907 keith@torvelgroup.com www.TorvelGroup.com

Industry/Entity Type

Real Estate

```html
<!DOCTYPE html>
<html lang="en">
<head>
<meta charset="utf-8">
<title>Torvel Group – Flexible and Focused Postcard</title>
<link rel="stylesheet" href="https://fonts.googleapis.com/css2?family=Montserrat:wght@400;700&display=swap">
<style>
  :root {
    --backdrop: #c8c8c8;
    --card: #ffffff;
    --ink: #2f2f2f;
    --headline: #ffffff;
    --brand-blue: #1b4c9c;
    --wave-light: #4f93d8;
    --wave-dark: #3e62b8;
    --sky-top: #4f86d2;
    --sky-low: #b8cde8;
    --brick: #9a5a44;
    --lawn: #6c8c48;
    --asphalt: #67686a;
  }
  * { margin: 0; padding: 0; box-sizing: border-box; }
  html, body {
    width: 1200px;
    height: 820px;
    overflow: hidden;
    background: var(--backdrop);
    font-family: "Montserrat", Arial, sans-serif;
  }
  .postcard {
    position: absolute;
    left: 67px;
    top: 67px;
    width: 1066px;
    height: 685px;
    background: var(--card);
    overflow: hidden;
  }
  .hero-photo {
    position: absolute;
    inset: 0 0 140px 0;
    background: linear-gradient(180deg,
      var(--sky-top) 0%,
      var(--sky-low) 20%,
      var(--brick) 33%,
      var(--brick) 42%,
      var(--lawn) 47%,
      var(--asphalt) 58%,
      var(--asphalt) 100%);
  }
  .wave-band {
    position: absolute;
    left: 0;
    top: 0;
    width: 1066px;
    height: 685px;
  }
  .headline {
    position: absolute;
    left: 79px;
    top: 284px;
    color: var(--headline);
    font-weight: 700;
    font-size: 62px;
    line-height: 70px;
    letter-spacing: 0.5px;
    text-shadow: 0 2px 6px rgba(0,0,0,0.45);
  }
  .headline .connector {
    font-weight: 400;
    font-size: 46px;
    letter-spacing: 0;
  }
  .intro-copy {
    position: absolute;
    left: 73px;
    top: 558px;
    width: 560px;
    color: var(--ink);
    font-size: 19px;
    line-height: 27px;
  }
  .brand-name {
    position: absolute;
    left: 740px;
    top: 530px;
    width: 230px;
    text-align: center;
    color: var(--brand-blue);
    font-weight: 700;
    font-size: 40px;
    line-height: 48px;
    letter-spacing: 4px;
    text-transform: uppercase;
  }
</style>
</head>
<body>
  <main class="postcard">
    <div class="hero-photo" role="img" aria-label="Photograph of a two-building red brick medical office park with a tiled roof, landscaped lawns and a paved entry drive under a blue sky with clouds"></div>

    <svg class="wave-band" viewBox="0 0 1066 685" aria-hidden="true">
      <path d="M0 410 C 180 470, 330 520, 470 505 C 650 485, 830 360, 1066 348 L1066 685 L0 685 Z" fill="var(--wave-light)"/>
      <path d="M0 432 C 170 495, 330 535, 480 520 C 660 500, 850 395, 1066 392 L1066 685 L0 685 Z" fill="var(--wave-dark)"/>
      <path d="M0 452 C 170 515, 330 548, 470 540 C 660 525, 860 440, 1066 448 L1066 685 L0 685 Z" fill="var(--wave-light)"/>
      <path d="M0 468 C 170 530, 330 560, 470 555 C 660 545, 860 470, 1066 470 L1066 685 L0 685 Z" fill="var(--card)"/>
      <path d="M42 405 C 140 465, 300 480, 462 442 C 310 490, 160 488, 42 405 Z" fill="var(--wave-dark)"/>
    </svg>

    <h1 class="headline">FLEXIBLE <span class="connector">and</span><br>FOCUSED</h1>

    <p class="intro-copy">With years of experience developing healthcare projects across America, We are ready to tackle any challenge out client may present.</p>

    <div class="brand-name">Torvel<br>Group</div>
  </main>
</body>
</html>
```